Harbourline construction company Business card design

I need a business card design for my company. I have a logo but dont have business cards with our logo..

www.harbourlineconstructco.com.au

The logo is on the website

I need the same details as this design I have attached. we have changed the logo and colours. just like the website

Industry/Entity Type

Building

```html
<!DOCTYPE html>
<html lang="en">
<head>
<meta charset="utf-8">
<title>Harbourline Construction – Business Card</title>
<link rel="stylesheet" href="https://fonts.googleapis.com/css2?family=Open+Sans:wght@600;700&family=Tinos:wght@700&display=swap">
<style>
  :root {
    --paper: #ffffff;
    --brand-blue: #0a87c6;
    --tagline-blue: #1478b4;
    --ink-white: #ffffff;
  }
  html, body {
    margin: 0;
    padding: 0;
    overflow: hidden;
    background: var(--paper);
  }
  .card {
    position: relative;
    width: 1200px;
    height: 675px;
    overflow: hidden;
    background: var(--paper);
  }
  .card__panel {
    position: absolute;
    inset: 0;
    width: 1200px;
    height: 675px;
  }
  .brand {
    position: absolute;
    left: 92px;
    top: 150px;
    display: flex;
    align-items: center;
    gap: 22px;
  }
  .brand__mark {
    width: 70px;
    height: 70px;
    flex: none;
    background: var(--brand-blue);
  }
  .brand__name {
    margin: 0;
    font-family: "Tinos", "Times New Roman", serif;
    font-weight: 700;
    font-size: 40px;
    line-height: 44px;
    color: var(--brand-blue);
  }
  .tagline {
    position: absolute;
    left: 0;
    top: 458px;
    width: 682px;
    margin: 0;
    text-align: center;
    font-family: "Tinos", "Times New Roman", serif;
    font-weight: 700;
    font-size: 38px;
    line-height: 47px;
    color: var(--tagline-blue);
    text-shadow: 1px 2px 2px rgba(0, 0, 0, 0.45);
  }
  .person {
    position: absolute;
    right: 36px;
    top: 232px;
    text-align: right;
    color: var(--ink-white);
  }
  .person__name {
    margin: 0;
    font-family: "Tinos", "Times New Roman", serif;
    font-weight: 700;
    font-size: 39px;
    letter-spacing: 2px;
    line-height: 46px;
    text-shadow: 2px 2px 3px rgba(0, 0, 0, 0.6);
  }
  .person__role {
    margin: 4px 6px 0 0;
    font-family: "Open Sans", Arial, sans-serif;
    font-weight: 700;
    font-size: 29px;
    line-height: 36px;
    text-shadow: 1px 1px 2px rgba(0, 0, 0, 0.4);
  }
  .contacts {
    position: absolute;
    left: 756px;
    top: 463px;
    margin: 0;
    padding: 0;
    list-style: none;
    color: var(--ink-white);
    font-family: "Open Sans", Arial, sans-serif;
    font-weight: 700;
    font-size: 21px;
    letter-spacing: 0.5px;
  }
  .contacts__item {
    display: flex;
    align-items: center;
    height: 35.5px;
  }
  .contacts__item:last-child { margin-top: 4px; }
  .contacts__icon {
    width: 26px;
    height: 26px;
    margin-right: 24px;
    flex: none;
  }
</style>
</head>
<body>
<main class="card">
  <svg class="card__panel" viewBox="0 0 1200 675" aria-hidden="true">
    <defs>
      <filter id="panel-shadow" x="-20%" y="-10%" width="140%" height="120%">
        <feDropShadow dx="-10" dy="4" stdDeviation="9" flood-color="#000" flood-opacity="0.55"/>
      </filter>
    </defs>
    <polygon points="887,0 1200,0 1200,675 655,675" fill="#0a87c6" filter="url(#panel-shadow)"/>
  </svg>

  <div class="brand">
    <span class="brand__mark"></span>
    <p class="brand__name">Harbourline<br>Construction</p>
  </div>

  <p class="tagline">New Homes-Additions &amp; Renovations<br>Domestic&amp;Commercial Builders</p>

  <div class="person">
    <p class="person__name">MAREK DOLAN</p>
    <p class="person__role">Director</p>
  </div>

  <ul class="contacts">
    <li class="contacts__item">
      <svg class="contacts__icon" viewBox="0 0 24 24" aria-hidden="true"><path d="M6 3l3 4-2 2c1 3 3 5 6 6l2-2 4 3-2 3C10 19 5 14 4 5z" fill="#fff"/></svg>
      <span>08 94126630</span>
    </li>
    <li class="contacts__item">
      <svg class="contacts__icon" viewBox="0 0 24 24" aria-hidden="true"><rect x="7" y="2.5" width="10" height="19" rx="1.5" fill="none" stroke="#fff" stroke-width="2"/><circle cx="12" cy="18" r="1.2" fill="#fff"/></svg>
      <span>08 94126630</span>
    </li>
    <li class="contacts__item">
      <svg class="contacts__icon" viewBox="0 0 24 24" aria-hidden="true"><rect x="7" y="3" width="10" height="6" fill="none" stroke="#fff" stroke-width="1.8"/><rect x="3" y="9" width="18" height="8" rx="1.5" fill="none" stroke="#fff" stroke-width="1.8"/><rect x="7" y="14" width="10" height="6" fill="#0a87c6" stroke="#fff" stroke-width="1.8"/></svg>
      <span>0455 218 604</span>
    </li>
    <li class="contacts__item">
      <svg class="contacts__icon" viewBox="0 0 24 24" aria-hidden="true"><rect x="3" y="5" width="18" height="14" fill="none" stroke="#fff" stroke-width="1.8"/><path d="M3 5l9 8 9-8M3 19l7-7M21 19l-7-7" fill="none" stroke="#fff" stroke-width="1.8"/></svg>
      <span>Harbourlineco@mailbox.com</span>
    </li>
  </ul>
</main>
</body>
</html>
```